Ledgerwise 540 for Tavlo

We are looking to design a page for the mobile app. The app is intended for financial professionals and is based on a successful desktop application. The existing design will serve as a very rough guideline, but we are open to hearing ideas.
Uploaded file #1 contains a screenshot of the existing design. The workflow is as follows:
The user picks a portfolio from the Dropdown below portfolio.
The user picks a Loss Threshold, which will dictate what gets onto the bubble chart below.
Once the bubble on the chart is clicked, a text box pops up with the description of the particular crisis that the bubble represents.
Once the bubble is clicked, the right hand side bar charts are populated with moves relevant to this scenario.
The left hand pane contains two text boxes. The lower one is particularly important, because the user is able to remove scenarios or add scenarios (screen #2). Removing scenarios is simple.
Adding scenarios brings up a wizard (screen #3). It also needs to be designed consistently with the front page of the app. The wizard has different clickable categories going down the column on the left and in a row on the top. The user can pick some or all of these categories.

Notes: The app should be designed for landscape mode only. The key to keep in mind is how the user will select bubbles on the chart. Right now, it is quite easy, but with the touchscreen it may be more complicated, so please keep that in mind when designing the chart (it should still be some version of the similar chart).
*As a first pass, please submit your idea of the concept (layout/colors/buttons) without the detailed design. We will choose 1-3 concepts and then the detailed work will take place with a much higher chance of a payout.
Updates

Thank you for the first two sketches. The second one by bertrand appears to be a bit more mobile app oriented, though we are still considering both and waiting for other submissions. One request, could you rework the sketches to include a bit more of dark blue as a background?  \

Bertrand, I think that the bubbles are too small and they are missing some volume effects. Could you make them a bit more prominent (and pick some form of dark blue background) and change the color to see if they will stand out better?
 

Industry/Entity Type

Financial

Requirements
Must have
• The general outline for the bubble chart must be retained. But the actual execution may differ significantly. We are open to seeing different ideas.
The winning design will also get a contract to design the rest of the application (2 more screens), which will be worth the same as the original design.

```html
<!DOCTYPE html>
<html lang="en">
<head>
<meta charset="utf-8">
<title>Ledgerwise 540 for Tavlo – Stress Scenario Screens</title>
<link href="https://fonts.googleapis.com/css2?family=Arimo:wght@400;700&display=swap" rel="stylesheet">
<style>
:root{
  --page:#ffffff;
  --status:#000000;
  --status-text:#ffffff;
  --header-top:#2fb6ee;
  --header-bottom:#0a86cf;
  --toolbar-top:#f4f5f6;
  --toolbar-bottom:#d9dcdf;
  --label-blue:#1f7fc4;
  --field-top:#ffffff;
  --field-bottom:#d6d8da;
  --field-border:#8d9296;
  --chart-deep:#0d3a86;
  --chart-mid:#1a4fa0;
  --chart-edge:#2a63b6;
  --grid:#8fb0e0;
  --pane:#c9ccd0;
  --menu:#eceded;
  --menu-line:#cfd1d3;
  --menu-text:#6d7174;
  --menu-active:#1a8ad6;
  --table-head:#f6cc4f;
  --row-sel:#bcd6f2;
  --panel-title:#dfe6ee;
  --panel-title-text:#3a5f8a;
  --bar:#2b6ee8;
  --bar-dark:#1c3f9a;
  --bar-label:#cfdcf2;
  --plot-bg:#dfe8f7;
  --plot-ink:#102a5e;
  --pop:#1b98e0;
  --ink:#1d1d1d;
}
*{box-sizing:border-box;margin:0;padding:0}
html,body{width:1200px;height:846px;overflow:hidden;background:var(--page)}
body{position:relative;font-family:"Arimo",Arial,sans-serif;color:var(--ink)}

.screen{position:absolute;overflow:hidden;background:var(--chart-deep)}
.screen--tools{left:98px;top:82px;width:741px;height:553px}
.screen--chart{left:464px;top:282px;width:647px;height:486px;box-shadow:0 0 0 1px #2a2a2a}

.status-bar{position:absolute;left:0;top:0;right:0;height:16px;background:var(--status);color:var(--status-text);
  font-size:11px;font-weight:700;line-height:16px}
.status-bar .device{position:absolute;left:6px}
.status-bar .time{position:absolute;left:0;right:0;text-align:center}
.status-bar .battery{position:absolute;right:6px}
.status-bar .battery i{display:inline-block;width:20px;height:9px;border:1px solid #fff;vertical-align:-1px;margin-left:3px;padding:1px}
.status-bar .battery i b{display:block;width:30%;height:100%;background:#fff}

.app-header{position:absolute;left:0;right:0;top:16px;background:linear-gradient(var(--header-top),var(--header-bottom))}

.toolbar{position:absolute;right:0;background:linear-gradient(var(--toolbar-top),var(--toolbar-bottom));border-bottom:1px solid #9aa1a7}
.field{position:absolute}
.field label{display:block;font-size:7px;color:var(--label-blue);font-weight:700;text-transform:uppercase;margin-bottom:2px;text-align:center;white-space:nowrap}
.field label.left{text-align:left}
.field label b{color:var(--ink);font-weight:400}
.select{position:relative;height:17px;border:1px solid var(--field-border);border-radius:3px;background:linear-gradient(var(--field-top),var(--field-bottom));font-size:8px;line-height:15px;padding-left:5px;white-space:nowrap;overflow:hidden}
.select::after{content:"";position:absolute;right:0;top:0;bottom:0;width:14px;background:linear-gradient(#a9aeb3,#7d8287);border-left:1px solid var(--field-border)}
.select::before{content:"";position:absolute;right:4px;top:6px;border:3px solid transparent;border-top:4px solid #fff;z-index:1}
.button{height:17px;border:1px solid var(--field-border);border-radius:3px;background:linear-gradient(var(--field-top),var(--field-bottom));font-size:8px;line-height:15px;text-align:center}

.screen--chart .field label{font-size:6px}
.screen--chart .select,.screen--chart .button{height:13px;line-height:11px;font-size:7px}
.screen--chart .select::after{width:11px}
.screen--chart .select::before{right:3px;top:4px}

/* tools screen */
.side-pane{position:absolute;left:0;top:16px;width:230px;bottom:0;background:var(--pane)}
.side-pane .app-header{top:0;height:44px}
.main-menu{position:absolute;left:4px;top:47px;width:222px;height:252px;background:var(--menu);border-radius:6px;box-shadow:0 1px 3px rgba(0,0,0,.35);list-style:none;overflow:hidden}
.main-menu li{height:42px;line-height:42px;padding-left:14px;font-size:17px;color:var(--menu-text);border-bottom:1px solid var(--menu-line)}
.main-menu li:last-child{border-bottom:0}
.main-menu li.is-active{color:var(--menu-active);background:linear-gradient(#f4f5f5,#dcdfe1)}

.data-panel{position:absolute;left:2px;width:226px;background:#fff;font-size:9px}
.data-panel .dock{height:13px;line-height:13px;padding-left:3px;background:#f2f3f4;border-bottom:1px solid #aab}
.data-panel .dock span{float:right;margin-right:4px}
.data-panel h3{font-size:9px;font-weight:700;color:var(--panel-title-text);background:var(--panel-title);height:15px;line-height:15px;padding-left:4px;border-bottom:1px solid #a9b6c4}
.data-table{width:100%;border-collapse:collapse;table-layout:fixed}
.data-table th{background:var(--table-head);font-weight:400;text-align:left;padding:0 3px;height:15px;border:1px solid #c59e25;white-space:nowrap;overflow:hidden}
.data-table td{height:15px;padding:0 3px;border-bottom:1px solid #e3e3e3;white-space:nowrap;overflow:hidden}
.data-table td.num{text-align:right}
.data-table tr.is-selected td{background:var(--row-sel)}
.data-panel .filler{height:13px;background:#bfc1c3}
.search-row{display:flex;gap:4px;padding:3px 3px}
.search-row .input{flex:1;height:15px;border:1px solid #9aa0a6;background:#fff;font-size:9px;line-height:13px;text-align:right;padding-right:4px}
.search-row .button{width:36px;height:15px;line-height:13px}

.chart-area{position:absolute;background:linear-gradient(135deg,var(--chart-mid),var(--chart-deep))}
.chart-frame{position:absolute;border:1px solid var(--chart-edge);border-radius:8px;background:linear-gradient(160deg,#1c4c9c,#123f8a)}

/* chart screen */
.key-toggle{position:absolute;right:6px;top:8px;font-size:7px;text-align:right;line-height:9px;padding-right:14px}
.key-toggle i{position:absolute;right:0;top:4px;width:10px;height:10px;border:1px solid #555;background:#fff;font-style:normal;font-size:9px;line-height:8px;text-align:center}
.side-charts{position:absolute;right:0;width:161px;background:#1a4c9c;border-left:2px solid #0b2f6e}
.bubble-note{position:absolute;left:183px;top:121px;width:123px;background:var(--pop);border-radius:5px;color:#fff;font-size:7px;padding:5px 6px;box-shadow:0 1px 4px rgba(0,0,0,.4)}
.bubble-note h4{font-size:7px;font-weight:400;padding-bottom:4px;border-bottom:1px solid rgba(255,255,255,.5);margin-bottom:5px}
.bubble-note p{margin-bottom:7px}
.bubble-note a{display:block;text-align:right;color:#fff;text-decoration:underline}
.bubble-note::after{content:"";position:absolute;left:14px;bottom:-7px;border:7px solid transparent;border-bottom:0;border-top-color:var(--pop)}
.scenario-bubble{position:absolute;left:197px;top:175px;width:14px;height:14px;border-radius:50%;background:radial-gradient(circle at 40% 35%,#ffffff,#c9d4e4);box-shadow:0 0 3px rgba(255,255,255,.6)}
</style>
</head>
<body>

<!-- Tools screen -->
<section class="screen screen--tools" aria-label="Tools screen">
  <div class="status-bar"><span class="device">Tavlo</span><span class="time">4:20 AM</span><span class="battery">32 %<i><b></b></i></span></div>
  <div class="app-header" style="height:44px"></div>

  <div class="toolbar" style="left:230px;top:60px;height:38px">
    <div class="field" style="left:6px;top:4px;width:67px"><label>Portfolio date</label><div class="select">6/18/2013</div></div>
    <div class="field" style="left:80px;top:4px;width:88px"><label>Portfolio</label><div class="select">KRV AA</div></div>
    <div class="field" style="left:176px;top:4px;width:67px"><label>Currency</label><div class="select">6/18/2013</div></div>
    <div class="field" style="left:252px;top:4px;width:90px"><label class="left">Model date: <b>06/12/2013</b></label><div class="button">Read model</div></div>
  </div>

  <div class="chart-area" style="left:230px;top:98px;right:0;bottom:0">
    <div class="chart-frame" style="left:10px;top:10px;right:10px;bottom:10px">
      <svg width="490" height="435" aria-hidden="true">
        <g stroke="var(--grid)" stroke-width="1" opacity=".8">
          <line x1="20" y1="20" x2="20" y2="420"/><line x1="48" y1="20" x2="48" y2="420"/><line x1="76" y1="20" x2="76" y2="420"/><line x1="104" y1="20" x2="104" y2="420"/><line x1="132" y1="20" x2="132" y2="420"/><line x1="160" y1="20" x2="160" y2="420"/><line x1="188" y1="20" x2="188" y2="420"/>
          <line x1="20" y1="20" x2="490" y2="20"/><line x1="20" y1="48" x2="490" y2="48"/><line x1="20" y1="76" x2="490" y2="76"/><line x1="20" y1="104" x2="490" y2="104"/><line x1="20" y1="132" x2="490" y2="132"/><line x1="20" y1="160" x2="490" y2="160"/><line x1="20" y1="188" x2="490" y2="188"/><line x1="20" y1="216" x2="490" y2="216"/><line x1="20" y1="244" x2="490" y2="244"/><line x1="20" y1="272" x2="490" y2="272"/><line x1="20" y1="300" x2="490" y2="300"/><line x1="20" y1="328" x2="490" y2="328"/><line x1="20" y1="356" x2="490" y2="356"/><line x1="20" y1="384" x2="490" y2="384"/>
        </g>
      </svg>
    </div>
  </div>

  <aside class="side-pane">
    <div class="app-header"></div>
    <ul class="main-menu">
      <li>New Tab</li>
      <li>Current Tab</li>
      <li>Saved Tab</li>
      <li class="is-active">Tools</li>
      <li>Load Models</li>
      <li>About</li>
    </ul>

    <div class="data-panel" style="top:302px">
      <div class="dock">Shocks<span>&#9632;</span></div>
      <h3>Shocks</h3>
      <table class="data-table">
        <colgroup><col style="width:84px"><col style="width:56px"><col></colgroup>
        <tr><th>Name</th><th>Type</th><th>Shock</th></tr>
        <tr class="is-selected"><td>UNITED STATES</td><td>Equity Inde</td><td class="num">-15</td></tr>
        <tr><td>Gold</td><td>Macro/Styl</td><td class="num">60</td></tr>
        <tr><td>3 Years US Govern</td><td>Interest Ra</td><td class="num">3</td></tr>
        <tr><td>30 Years US Gover</td><td>Interest Ra</td><td class="num">3</td></tr>
      </table>
      <div class="filler"></div>
    </div>

    <div class="data-panel" style="top:445px;bottom:0">
      <h3>Current Scenario</h3>
      <div class="search-row"><div class="input">&#10005; &#9662;</div><div class="button">Find</div></div>
      <table class="data-table">
        <colgroup><col style="width:112px"><col style="width:44px"><col style="width:48px"><col></colgroup>
        <tr><th>Name</th><th>Loss</th><th>Correlation</th><th>Pla</th></tr>
        <tr><td>US Treasury Interest</td><td class="num">-21.57</td><td class="num">-21.57</td><td></td></tr>
        <tr><td>Stagflation Severe</td><td class="num">-18.82</td><td class="num">-18.82</td><td></td></tr>
      </table>
    </div>
  </aside>
</section>

<!-- Chart screen -->
<section class="screen screen--chart" aria-label="Scenario bubble chart screen">
  <div class="status-bar"><span class="device">Tavlo</span><span class="time">4:20 AM</span><span class="battery">32 %<i><b></b></i></span></div>
  <div class="app-header" style="height:36px"></div>

  <div class="toolbar" style="left:0;top:52px;height:35px">
    <div class="field" style="left:6px;top:5px;width:57px"><label>Portfolio date</label><div class="select">6/18/2013</div></div>
    <div class="field" style="left:72px;top:5px;width:78px"><label>Portfolio</label><div class="select">KRV AA</div></div>
    <div class="field" style="left:157px;top:5px;width:58px"><label>Currency</label><div class="select">6/18/2013</div></div>
    <div class="field" style="left:223px;top:5px;width:78px"><label class="left">Model date: <b>06/12/2013</b></label><div class="button">Read model</div></div>
    <div class="key-toggle">Only Key<br>Scenarios<i>&#10003;</i></div>
  </div>

  <div class="chart-area" style="left:0;top:87px;right:162px;bottom:0">
    <div class="chart-frame" style="left:5px;top:6px;right:6px;bottom:6px">
      <svg width="474" height="387" aria-hidden="true">
        <g stroke="var(--grid)" stroke-width="1" opacity=".85">
          <line x1="20" y1="20" x2="20" y2="360"/><line x1="48" y1="20" x2="48" y2="360"/><line x1="76" y1="20" x2="76" y2="360"/><line x1="104" y1="20" x2="104" y2="360"/><line x1="132" y1="20" x2="132" y2="360"/><line x1="160" y1="20" x2="160" y2="360"/><line x1="188" y1="20" x2="188" y2="360"/><line x1="216" y1="20" x2="216" y2="360"/><line x1="244" y1="20" x2="244" y2="360"/><line x1="272" y1="20" x2="272" y2="360"/><line x1="300" y1="20" x2="300" y2="360"/><line x1="328" y1="20" x2="328" y2="360"/><line x1="356" y1="20" x2="356" y2="360"/><line x1="384" y1="20" x2="384" y2="360"/><line x1="412" y1="20" x2="412" y2="360"/><line x1="440" y1="20" x2="440" y2="360"/>
          <line x1="20" y1="20" x2="440" y2="20"/><line x1="20" y1="41" x2="440" y2="41"/><line x1="20" y1="62" x2="440" y2="62"/><line x1="20" y1="83" x2="440" y2="83"/><line x1="20" y1="104" x2="440" y2="104"/><line x1="20" y1="125" x2="440" y2="125"/><line x1="20" y1="146" x2="440" y2="146"/><line x1="20" y1="167" x2="440" y2="167"/><line x1="20" y1="188" x2="440" y2="188"/><line x1="20" y1="209" x2="440" y2="209"/><line x1="20" y1="230" x2="440" y2="230"/><line x1="20" y1="251" x2="440" y2="251"/><line x1="20" y1="272" x2="440" y2="272"/><line x1="20" y1="293" x2="440" y2="293"/><line x1="20" y1="314" x2="440" y2="314"/><line x1="20" y1="335" x2="440" y2="335"/><line x1="20" y1="356" x2="440" y2="356"/>
        </g>
      </svg>
      <div class="bubble-note">
        <h4>Name: Stagflation Severe</h4>
        <p>Lorem ipsum dolor sit amet</p>
        <a>Close</a>
      </div>
      <div class="scenario-bubble"></div>
    </div>
  </div>

  <div class="side-charts" style="top:87px;height:200px;border-bottom:2px solid #0b2f6e">
    <svg width="159" height="198" font-family="Arimo, Arial, sans-serif" font-size="5" aria-label="Top asset moves bar chart">
      <rect x="58" y="6" width="96" height="160" fill="var(--plot-bg)"/>
      <g fill="var(--bar-label)" text-anchor="end">
        <text x="55" y="15">BLT 6 02/15/27</text><text x="55" y="30">CRN 8 02/15/27</text><text x="55" y="45">HVN 5 12/31/19</text><text x="55" y="60">DLN 5 12/31/19</text><text x="55" y="75">MRD 7 01/15/19</text><text x="55" y="90">ARX Float 01/26</text><text x="55" y="105">QSL 7 01/15/19</text><text x="55" y="120">PLM 12 01/15/19</text><text x="55" y="135">KWE 10 01/15/19</text><text x="55" y="150">FNT 10 01/15/19</text>
      </g>
      <g fill="var(--bar)">
        <rect x="58" y="9" width="80" height="9"/><rect x="58" y="24" width="70" height="9"/><rect x="58" y="39" width="52" height="9"/><rect x="58" y="54" width="44" height="9"/><rect x="58" y="69" width="36" height="9"/><rect x="58" y="84" width="30" height="9"/><rect x="58" y="99" width="26" height="9"/><rect x="58" y="114" width="22" height="9"/><rect x="58" y="129" width="16" height="9"/><rect x="58" y="144" width="12" height="9"/>
      </g>
      <g fill="#fff" stroke="var(--plot-ink)" stroke-width=".5">
        <rect x="138" y="9" width="14" height="9"/><rect x="128" y="24" width="14" height="9"/><rect x="110" y="39" width="14" height="9"/><rect x="102" y="54" width="14" height="9"/><rect x="94" y="69" width="14" height="9"/><rect x="88" y="84" width="14" height="9"/><rect x="84" y="99" width="14" height="9"/><rect x="80" y="114" width="14" height="9"/><rect x="74" y="129" width="14" height="9"/><rect x="70" y="144" width="14" height="9"/>
      </g>
      <g fill="var(--plot-ink)" font-size="4.5" text-anchor="middle">
        <text x="145" y="15.5">0.03</text><text x="135" y="30.5">0.03</text><text x="117" y="45.5">0.02</text><text x="109" y="60.5">0.02</text><text x="101" y="75.5">0.02</text><text x="95" y="90.5">0.01</text><text x="91" y="105.5">0.01</text><text x="87" y="120.5">0.01</text><text x="81" y="135.5">0.01</text><text x="77" y="150.5">0.00</text>
      </g>
      <g fill="var(--plot-bg)" font-size="4.5" text-anchor="middle">
        <text x="61" y="175">0.00</text><text x="78" y="175">0.01</text><text x="96" y="175">0.02</text><text x="114" y="175">0.03</text><text x="132" y="175">0.04</text><text x="150" y="175">0.05</text>
      </g>
    </svg>
  </div>

  <div class="side-charts" style="top:289px;bottom:0">
    <svg width="159" height="197" font-family="Arimo, Arial, sans-serif" font-size="5" aria-label="Bottom asset moves bar chart">
      <rect x="58" y="6" width="96" height="172" fill="var(--plot-bg)"/>
      <line x1="106" y1="6" x2="106" y2="178" stroke="var(--plot-ink)" stroke-width=".5"/>
      <g fill="var(--bar-label)" text-anchor="end">
        <text x="55" y="15">OKT 7 03/05/27</text><text x="55" y="29">SOV T 03/05/27</text><text x="55" y="43">TIP 0 12/31/19</text><text x="55" y="57">TIP 0 12/31/20</text><text x="55" y="71">SOV N 03/05/19</text><text x="55" y="85">KRV 2005 AA</text><text x="55" y="99">SOV R 03/05/22</text><text x="55" y="113">TIP 0 04/15/29</text><text x="55" y="127">TIP 3 04/15/29</text><text x="55" y="141">VSR 5 12/31/19</text><text x="55" y="155">NRD 4 12/31/19</text><text x="55" y="169">EQ Broad Idx</text>
      </g>
      <g fill="var(--bar)">
        <rect x="106" y="9" width="18" height="8"/><rect x="106" y="23" width="16" height="8"/><rect x="106" y="37" width="14" height="8"/><rect x="106" y="51" width="14" height="8"/><rect x="106" y="65" width="12" height="8"/><rect x="106" y="79" width="10" height="8"/><rect x="106" y="93" width="10" height="8"/><rect x="106" y="107" width="8" height="8"/><rect x="106" y="121" width="8" height="8"/>
        <rect x="90" y="135" width="16" height="8"/><rect x="80" y="149" width="26" height="8"/><rect x="60" y="163" width="46" height="8" fill="var(--bar-dark)"/>
      </g>
      <g fill="#fff" stroke="var(--plot-ink)" stroke-width=".5">
        <rect x="126" y="9" width="14" height="8"/><rect x="124" y="23" width="14" height="8"/><rect x="122" y="37" width="14" height="8"/><rect x="122" y="51" width="14" height="8"/><rect x="120" y="65" width="14" height="8"/><rect x="118" y="79" width="14" height="8"/><rect x="118" y="93" width="14" height="8"/><rect x="116" y="107" width="14" height="8"/><rect x="116" y="121" width="14" height="8"/>
        <rect x="76" y="135" width="14" height="8"/><rect x="66" y="149" width="14" height="8"/><rect x="62" y="163" width="14" height="8"/>
      </g>
      <g fill="var(--plot-ink)" font-size="4.5" text-anchor="middle">
        <text x="133" y="15">0.20</text><text x="131" y="29">0.18</text><text x="129" y="43">0.15</text><text x="129" y="57">0.15</text><text x="127" y="71">0.12</text><text x="125" y="85">0.10</text><text x="125" y="99">0.10</text><text x="123" y="113">0.08</text><text x="123" y="127">0.08</text><text x="83" y="141">-0.17</text><text x="73" y="155">-0.27</text><text x="69" y="169">-0.48</text>
      </g>
      <g fill="var(--plot-bg)" font-size="4.5" text-anchor="middle">
        <text x="61" y="187">-0.5</text><text x="76" y="187">-0.3</text><text x="91" y="187">-0.2</text><text x="106" y="187">0</text><text x="121" y="187">0.2</text><text x="136" y="187">0.3</text><text x="151" y="187">0.5</text>
      </g>
    </svg>
  </div>
</section>

</body>
</html>
```